Silver Birch Decorators Banner

Create a banner that displays and reinforces Silver Birch Decorators’ brand identity while promoting our interior painting services. The banner will be displayed at indoor venues through the winter. The design should be clean, professional, and visually recognizable to both new and returning customers. See attached design brief & logo source files.

```html
<!DOCTYPE html>
<html lang="en">
<head>
<meta charset="utf-8">
<title>Silver Birch Decorators Banner</title>
<link rel="stylesheet" href="https://fonts.googleapis.com/css2?family=Poppins:wght@600;700;800&display=swap">
<style>
  :root {
    --stage: #8c8c8c;
    --paper: #ffffff;
    --green: #5f8446;
    --green-light: #6f9a55;
    --ink: #3c3c3c;
    --accent: #e01b1b;
  }
  * { margin: 0; padding: 0; box-sizing: border-box; }
  html, body { width: 1200px; height: 753px; overflow: hidden; background: var(--stage); }
  body { position: relative; font-family: "Poppins", Arial, sans-serif; }

  .banner {
    position: absolute; left: 95px; top: 162px;
    width: 1041px; height: 416px;
    background: var(--paper); overflow: hidden;
  }
  .banner-art { position: absolute; inset: 0; width: 1041px; height: 416px; }

  .brand {
    position: absolute; left: 55px; top: 44px;
    display: flex; align-items: center; gap: 12px;
    color: var(--green); font-weight: 800; font-size: 27px; line-height: 1.05;
  }
  .brand-dot { width: 22px; height: 22px; border-radius: 50%; background: var(--green); flex: none; }

  .headline {
    position: absolute; left: 272px; top: 26px;
    font-weight: 800; font-size: 42px; line-height: 40px;
    letter-spacing: -1px; color: var(--green); text-transform: uppercase;
  }
  .headline .since { color: var(--ink); display: block; }

  .services-title {
    position: absolute; left: 55px; top: 172px;
    color: var(--paper); font-weight: 700; font-size: 26px; letter-spacing: -0.3px;
  }
  .service {
    position: absolute; top: 218px; transform: translateX(-50%);
    display: flex; flex-direction: column; align-items: center; gap: 8px;
    color: var(--paper); font-weight: 600; font-size: 18px; white-space: nowrap;
  }
  .service-icon { width: 38px; height: 38px; }

  .cta {
    position: absolute; left: 55px; top: 310px;
    color: var(--ink); font-weight: 700; font-size: 31px; letter-spacing: -0.5px;
  }
  .cta .free { color: var(--accent); }
  .url {
    position: absolute; left: 55px; top: 346px;
    color: var(--ink); font-weight: 800; font-size: 42px; letter-spacing: -0.5px;
  }
  .url .domain { color: var(--green); }
</style>
</head>
<body>
  <section class="banner">
    <svg class="banner-art" viewBox="0 0 1041 416" aria-hidden="false">
      <defs>
        <linearGradient id="interior" x1="0" y1="0" x2="1" y2="1">
          <stop offset="0" stop-color="#3a3530"/>
          <stop offset="0.35" stop-color="#d8cfc2"/>
          <stop offset="0.7" stop-color="#c9b9a2"/>
          <stop offset="1" stop-color="#5a4e44"/>
        </linearGradient>
      </defs>
      <polygon class="service-band" points="0,162 640,162 612,220 652,300 0,300" fill="var(--green)"/>
      <polygon class="photo-edge" points="728,0 745,0 664,206 698,416 681,416 647,206" fill="var(--green-light)"/>
      <polygon class="photo" role="img" aria-label="Photo of a bright painted interior with an open staircase, wooden beams and a globe chandelier"
               points="745,0 1041,0 1041,416 698,416 664,206" fill="url(#interior)"/>
    </svg>

    <div class="brand"><span class="brand-dot"></span><span>Silver Birch<br>Decorators</span></div>

    <h1 class="headline">Trusted Local<br>Professionals,<span class="since">Since 2005</span></h1>

    <h2 class="services-title">INTERIOR PAINTING SERVICES</h2>

    <div class="service" style="left:88px">
      <svg class="service-icon" viewBox="0 0 38 38"><circle cx="19" cy="19" r="18" fill="#fff"/><rect x="11" y="10" width="14" height="7" rx="1.5" fill="var(--green)"/><path d="M25 13h3v7h-9v4" fill="none" stroke="var(--green)" stroke-width="2"/><rect x="17" y="24" width="4" height="6" fill="var(--green)"/></svg>
      <span>Walls</span>
    </div>
    <div class="service" style="left:186px">
      <svg class="service-icon" viewBox="0 0 38 38"><circle cx="19" cy="19" r="18" fill="#fff"/><rect x="10" y="10" width="18" height="3" fill="var(--green)"/><path d="M12 13v14M26 13v14M10 27h18" stroke="var(--green)" stroke-width="2.5" fill="none"/></svg>
      <span>Ceilings</span>
    </div>
    <div class="service" style="left:274px">
      <svg class="service-icon" viewBox="0 0 38 38"><circle cx="19" cy="19" r="18" fill="#fff"/><path d="M11 27l10-10" stroke="var(--green)" stroke-width="3"/><rect x="19" y="9" width="9" height="9" transform="rotate(45 23.5 13.5)" fill="var(--green)"/></svg>
      <span>Trim</span>
    </div>
    <div class="service" style="left:374px">
      <svg class="service-icon" viewBox="0 0 38 38"><circle cx="19" cy="19" r="18" fill="#fff"/><rect x="10" y="9" width="18" height="20" rx="1.5" fill="none" stroke="var(--green)" stroke-width="2.5"/><path d="M19 9v20" stroke="var(--green)" stroke-width="2"/><circle cx="16.5" cy="19" r="1.3" fill="var(--green)"/><circle cx="21.5" cy="19" r="1.3" fill="var(--green)"/></svg>
      <span>Cabinets</span>
    </div>
    <div class="service" style="left:510px">
      <svg class="service-icon" viewBox="0 0 38 38"><circle cx="19" cy="19" r="18" fill="#fff"/><rect x="11" y="10" width="16" height="18" fill="none" stroke="var(--green)" stroke-width="2.5"/><path d="M14 22l4-4 3 3 4-5" fill="none" stroke="var(--green)" stroke-width="2"/></svg>
      <span>Drywall Repair</span>
    </div>

    <p class="cta">BOOK A <span class="free">FREE ESTIMATE</span> AT</p>
    <p class="url">www.<span class="domain">silverbirchdeco</span>.com</p>
  </section>
</body>
</html>
```